Florida-based Coastal Landscaping Comapny Needs Postcard Designs

We are a newly established Florida-based, coastal landscaping company that is looking for some really innovative postcards that we can use to get our name our to affluent consumers that live on the coast of Florida (think on the beach) and small to medium sized businesses in the same area. We will be sending out 100s of thousands of these, so need a great design

Target Market(s)

Affluent consumers and small to medium sized businesses

Industry/Entity Type

Landscaping

Font styles to use
Sans Serif

Colors

Designer to choose colors to be used in the design.

Requirements
Must have
• Florida - looking, island looking / paradise, but incorporate landscaping themes
• Need to say something about "Enjoy your yard this summer" or something relating to summer, landscapes and florida
• and would like to make two offers $50.00 off with signing up for one of our routine maintenance programs, or 1 free landscape inspection
Should not have
• Regular generic lawn company designs. We are a top tier landscape design / build plus maintenance firm, so not your mom and pop lawn mowing company

```html
<!DOCTYPE html>
<html lang="en">
<head>
<meta charset="utf-8">
<title>Shorevale Summer Postcards</title>
<link rel="stylesheet" href="https://fonts.googleapis.com/css2?family=Montserrat:wght@400;600;700;800&family=Monoton&family=Oswald:wght@500;600;700&display=swap">
<style>
  :root{
    --board:#808080;
    --board-label:#f2f2f2;
    --ink:#111111;
    --red:#c8102e;
    --offer-red:#e8202a;
    --cyan:#1aa6d8;
    --teal:#1d8fb3;
    --wave:#1fa3c9;
    --wave-light:#6fcbe6;
    --paper:#fbfaf4;
    --yellow:#ffe600;
    --line:#9a9a9a;
  }
  *{margin:0;padding:0;box-sizing:border-box}
  html,body{width:1200px;height:895px;overflow:hidden;background:var(--board)}
  .board{position:relative;width:1200px;height:895px;background:var(--board);font-family:"Montserrat",sans-serif}
  .card{position:absolute;width:496px;height:385px;overflow:hidden;background:var(--paper);box-shadow:0 4px 10px rgba(0,0,0,.35)}
  .front-a{left:22px;top:29px}.front-b{left:622px;top:29px}
  .back-a{left:22px;top:442px}.back-b{left:622px;top:442px}

  .side-label{position:absolute;color:var(--board-label);font-size:22px;font-weight:400;transform:rotate(-90deg);transform-origin:center;white-space:nowrap;font-family:"Montserrat",sans-serif}
  .sample-label{position:absolute;top:848px;color:var(--board-label);font-size:25px;width:200px;text-align:center;font-family:"Montserrat",sans-serif}

  /* front */
  .front-sky{position:absolute;inset:0;background:linear-gradient(180deg,#d7eef8 0%,#eef7fa 45%,var(--paper) 80%)}
  .front-photo{position:absolute;left:276px;top:0;width:220px;height:385px;
    background:linear-gradient(180deg,#5fa8dc 0%,#9fcbe6 25%,#f0c57a 42%,#c9a77c 55%,#9c8466 75%,rgba(251,250,244,0) 100%)}
  .enjoy{position:absolute;left:31px;top:31px;font-weight:800;font-size:62px;line-height:1;letter-spacing:1px;color:var(--ink);white-space:nowrap}
  .yard{position:absolute;left:33px;top:92px;font-weight:700;font-size:35px;line-height:1;color:#1d1d1d;white-space:nowrap}
  .season{position:absolute;left:78px;font-family:"Monoton",sans-serif;font-size:72px;line-height:1;white-space:nowrap}
  .season.sum{top:127px;color:var(--red)}
  .season.mer{top:189px;color:var(--ink)}
  .this{position:absolute;left:28px;top:130px;height:118px;writing-mode:vertical-rl;transform:rotate(180deg);
    font-weight:800;font-size:50px;color:var(--cyan);letter-spacing:-1px;line-height:1;white-space:nowrap}
  .brand{position:absolute;font-family:"Montserrat",sans-serif;font-weight:400;color:var(--teal);letter-spacing:1px;white-space:nowrap}
  .front-brand{left:31px;top:330px;font-size:31px;letter-spacing:2px}
  .site{position:absolute;font-size:10px;letter-spacing:3px;color:var(--teal);white-space:nowrap}

  /* back 1 */
  .back-wash{position:absolute;inset:0;background:linear-gradient(160deg,#cfe9f4 0%,#e4f3f8 50%,var(--paper) 78%)}
  .back-photo-a{position:absolute;left:0;top:0;width:330px;height:250px;
    background:linear-gradient(180deg,#c9e2f0 0%,#a9d3e8 35%,#4e93ad 55%,#d4e6ea 80%,rgba(251,250,244,0) 100%)}
  .stamp{position:absolute;left:400px;top:19px;width:74px;height:95px;border:1px solid #ffffff}
  .address-line{position:absolute;left:294px;width:180px;height:1px;background:var(--line)}
  .offer-a{position:absolute;left:0;top:226px;width:280px;text-align:center;color:#0f2a44}
  .offer-a .big{font-weight:700;font-size:19px;letter-spacing:.5px;line-height:1.2}
  .offer-a .big em{font-style:normal;color:var(--offer-red)}
  .offer-a .small{font-size:10.5px;color:var(--teal);line-height:1.3}
  .offer-a .or{font-size:12px;margin-top:4px;color:#333;line-height:1.2}
  .offer-a .free{font-weight:700;font-size:19px;letter-spacing:.5px;line-height:1.15}
  .offer-a .insp{font-size:13px;color:var(--teal);line-height:1.3}
  .waves{position:absolute;left:0;bottom:0}
  .back-a .brand{left:309px;top:322px;font-size:22px}
  .back-a .site{left:310px;top:358px}

  /* back 2 */
  .back-photo-b{position:absolute;left:0;top:0;width:300px;height:300px;
    background:linear-gradient(180deg,#cfe3ef 0%,#a8d0e5 30%,#4b8ea8 52%,#d6e8ec 78%,rgba(251,250,244,0) 100%)}
  .offer-panel{position:absolute;left:262px;top:0;width:234px;height:300px;background:radial-gradient(ellipse at 60% 45%,#ffffff 60%,rgba(255,255,255,0) 100%)}
  .offers-vert{position:absolute;left:270px;top:36px;height:62px;writing-mode:vertical-rl;transform:rotate(180deg);
    font-family:"Oswald",sans-serif;font-weight:700;font-size:20px;color:#0f2a44;line-height:1;white-space:nowrap}
  .price{position:absolute;left:296px;top:30px;font-family:"Oswald",sans-serif;font-weight:700;font-size:58px;line-height:1;color:var(--offer-red);letter-spacing:-1px;white-space:nowrap}
  .off-tag{position:absolute;left:462px;top:40px;width:24px;height:54px;border-radius:12px;background:var(--offer-red);color:#fff;
    writing-mode:vertical-rl;transform:rotate(180deg);font-family:"Oswald",sans-serif;font-weight:700;font-size:16px;text-align:center;line-height:24px}
  .offer-copy{position:absolute;left:266px;top:102px;width:230px;text-align:center;font-weight:700;font-size:14.5px;line-height:19px;color:var(--cyan)}
  .offer-or{position:absolute;left:266px;top:163px;width:230px;text-align:center;font-weight:600;font-size:13px;color:#111}
  .one{position:absolute;left:272px;top:168px;font-family:"Oswald",sans-serif;font-weight:700;font-size:112px;line-height:1;color:var(--offer-red)}
  .free-box{position:absolute;left:314px;top:186px;width:150px;height:90px;background:var(--offer-red);border-left:3px solid #fff;
    padding:1px 0 0 5px;font-family:"Oswald",sans-serif;font-weight:500;font-size:29px;line-height:29px;color:var(--yellow);white-space:nowrap}
  .back-b .brand{left:173px;top:306px;font-size:22px}
  .back-b .site{left:170px;top:340px}
</style>
</head>
<body>
<main class="board">

  <section class="card front-a">
    <div class="front-sky"></div>
    <div class="front-photo" role="img" aria-label="Lifeguard tower on a sunny Florida beach at sunset"></div>
    <div class="enjoy">ENJOY</div>
    <div class="yard">YOUR YARD</div>
    <div class="this">THIS</div>
    <div class="season sum">SUM</div>
    <div class="season mer">MER</div>
    <div class="brand front-brand">SHOREVALE</div>
  </section>

  <section class="card front-b">
    <div class="front-sky"></div>
    <div class="front-photo" role="img" aria-label="Lifeguard tower on a sunny Florida beach at sunset"></div>
    <div class="enjoy">ENJOY</div>
    <div class="yard">YOUR YARD</div>
    <div class="this">THIS</div>
    <div class="season sum">SUM</div>
    <div class="season mer">MER</div>
    <div class="brand front-brand">SHOREVALE</div>
  </section>

  <section class="card back-a">
    <div class="back-wash"></div>
    <div class="back-photo-a" role="img" aria-label="Woman with open arms facing the sea with seagulls"></div>
    <div class="stamp"></div>
    <div class="address-line" style="top:202px"></div>
    <div class="address-line" style="top:235px"></div>
    <div class="address-line" style="top:266px"></div>
    <svg class="waves" width="496" height="110" viewBox="0 0 496 110">
      <path d="M0 52 C80 78 200 90 278 48 L278 110 L0 110 Z" fill="var(--wave)"/>
      <path d="M0 72 C100 96 210 100 278 62 L278 110 L0 110 Z" fill="var(--wave-light)" opacity=".6"/>
    </svg>
    <div class="offer-a">
      <div class="big">OFFERS <em>$50.00</em> OFF</div>
      <div class="small">with signing up for one of our routine<br>maintenance programs</div>
      <div class="or">or</div>
      <div class="free">1 FREE LANDSCAPE</div>
      <div class="insp">inspection</div>
    </div>
    <div class="brand">SHOREVALE</div>
    <div class="site">www.shorevale.com</div>
  </section>

  <section class="card back-b">
    <div class="back-wash"></div>
    <div class="back-photo-b" role="img" aria-label="Woman with open arms facing the sea with seagulls"></div>
    <div class="offer-panel"></div>
    <div class="offers-vert">OFFERS</div>
    <div class="price">$50.00</div>
    <div class="off-tag">OFF</div>
    <div class="offer-copy">with signing up for one of<br>our routine maintenance<br>programs</div>
    <div class="offer-or">OR</div>
    <div class="one">1</div>
    <div class="free-box">FREE<br>LANDSCAPE<br>INSPECTION</div>
    <svg class="waves" width="496" height="90" viewBox="0 0 496 90">
      <path d="M0 40 C120 70 300 80 496 20 L496 90 L0 90 Z" fill="var(--wave)"/>
      <path d="M0 62 C140 86 320 84 496 44 L496 90 L0 90 Z" fill="var(--wave-light)" opacity=".6"/>
    </svg>
    <div class="brand">SHOREVALE</div>
    <div class="site">www.shorevale.com</div>
  </section>

  <div class="side-label" style="left:518px;top:210px">Front 1</div>
  <div class="side-label" style="left:1118px;top:210px">Front 1</div>
  <div class="side-label" style="left:526px;top:610px">Back</div>
  <div class="side-label" style="left:1126px;top:610px">Back</div>
  <div class="sample-label" style="left:172px">Sample 1</div>
  <div class="sample-label" style="left:772px">Sample 2</div>
</main>
</body>
</html>
```